Logo for Internal Medicine practice

I want a logo for my Internal Medicine practice, I would like it to be with my name on it which is Lucía Barrenechea Ruiz.

I would like the business card to say the following (it is in Spanish since my practice is in Spanish):

Lucía Barrenechea Ruiz
Medicina Interna
Cel. 5583617204
luciabarrenechearuiz@correovela.mx

Logo Text

Lucía Barrenechea

```html
<!DOCTYPE html>
<html lang="es">
<head>
<meta charset="utf-8">
<title>Lucía Barrenechea — Tarjeta de presentación</title>
<link rel="stylesheet" href="https://fonts.googleapis.com/css2?family=Cinzel:wght@600;700&family=Montserrat:wght@400;500&display=swap">
<style>
  :root {
    --backdrop: #2b2b2d;
    --card-white: #ffffff;
    --card-black: #141414;
    --ink: #111111;
    --brand-red: #e41e26;
    --brand-blue: #1f74bd;
    --stripe-black: #151515;
    --muted: #6b6b6b;
    --on-dark: #f2f2f2;
  }
  * { box-sizing: border-box; margin: 0; padding: 0; }
  html, body { width: 1200px; height: 900px; overflow: hidden; }
  body {
    background: var(--backdrop);
    position: relative;
    font-family: "Montserrat", sans-serif;
  }
  .card {
    position: absolute;
    left: 250px;
    width: 700px;
    height: 400px;
    border-radius: 28px;
    overflow: hidden;
  }
  .card--front { top: 40px; background: var(--card-white); }
  .card--back { top: 470px; background: var(--card-black); }

  .card__swooshes { position: absolute; inset: 0; width: 100%; height: 100%; }

  .brand {
    position: absolute;
    display: flex;
    align-items: center;
    gap: 14px;
  }
  .brand__dot {
    width: 22px; height: 22px;
    border-radius: 50%;
    background: var(--brand-blue);
    flex: none;
  }
  .brand__name {
    font-family: "Cinzel", serif;
    font-weight: 700;
    font-size: 38px;
    letter-spacing: 1px;
    white-space: nowrap;
  }
  .card--front .brand { left: 150px; top: 92px; }
  .card--front .brand__name { color: var(--brand-red); }
  .card--back .brand { left: 50%; top: 50%; transform: translate(-50%, -50%); }
  .card--back .brand__name { color: var(--on-dark); font-size: 44px; }

  .contact {
    position: absolute;
    left: 52px;
    top: 228px;
  }
  .contact__name {
    font-family: "Cinzel", serif;
    font-weight: 700;
    font-size: 27px;
    color: var(--ink);
    letter-spacing: 0.5px;
    line-height: 1.1;
  }
  .contact__role {
    font-size: 15px;
    font-weight: 500;
    color: var(--brand-red);
    letter-spacing: 6px;
    text-transform: uppercase;
    margin-top: 6px;
  }
  .contact__list { list-style: none; margin-top: 12px; }
  .contact__item {
    display: flex;
    align-items: center;
    gap: 12px;
    font-size: 19px;
    color: var(--ink);
    line-height: 1.45;
  }
  .contact__icon { width: 16px; height: 16px; flex: none; }
</style>
</head>
<body>

<section class="card card--front" aria-label="Anverso de la tarjeta">
  <svg class="card__swooshes" viewBox="0 0 700 400" aria-hidden="true">
    <path d="M700,80 C690,240 620,350 560,400 L700,400 Z" fill="var(--brand-blue)"/>
    <path d="M700,115 C676,258 585,360 505,400" fill="none" stroke="var(--brand-red)" stroke-width="16"/>
    <path d="M700,150 C666,275 565,366 452,400" fill="none" stroke="var(--stripe-black)" stroke-width="10"/>

    <path d="M0,300 C18,160 80,60 160,0 L0,0 Z" fill="var(--brand-blue)"/>
    <path d="M0,258 C22,150 82,66 192,0" fill="none" stroke="var(--brand-red)" stroke-width="16"/>
    <path d="M0,222 C26,128 92,52 222,0" fill="none" stroke="var(--stripe-black)" stroke-width="10"/>
  </svg>

  <div class="brand">
    <span class="brand__dot"></span>
    <span class="brand__name">Lucía Barrenechea</span>
  </div>

  <div class="contact">
    <p class="contact__name">LUCÍA BARRENECHEA RUIZ</p>
    <p class="contact__role">Medicina Interna</p>
    <ul class="contact__list">
      <li class="contact__item">
        <svg class="contact__icon" viewBox="0 0 16 16" aria-hidden="true">
          <rect x="2" y="2" width="12" height="12" rx="2" fill="none" stroke="var(--brand-red)" stroke-width="2"/>
        </svg>
        <span>5583617204</span>
      </li>
      <li class="contact__item">
        <svg class="contact__icon" viewBox="0 0 16 16" aria-hidden="true">
          <rect x="1" y="3" width="14" height="10" fill="var(--brand-red)"/>
          <path d="M1,3 L8,9 L15,3" fill="none" stroke="#fff" stroke-width="1.4"/>
        </svg>
        <span>luciabarrenechearuiz@correovela.mx</span>
      </li>
    </ul>
  </div>
</section>

<section class="card card--back" aria-label="Reverso de la tarjeta">
  <div class="brand">
    <span class="brand__dot"></span>
    <span class="brand__name">Lucía Barrenechea</span>
  </div>
</section>

</body>
</html>
```